Zielgruppe
Endkunde ist eine Immobilienfirma ((Bauträger)
Aufgabenstellung
Das Design soll für eine Präsentationsmappe erstellt werden und die Bemaßung sowie Farbigleit der vorgegebnen pdf-Datei beinhalten. Es soll in den Hausfarben , nebst den Backround in grau, gehalten werden.

```html
<!DOCTYPE html>
<html lang="de">
<head>
<meta charset="utf-8">
<title>Präsentationsmappe – Wertbau Elbland AG</title>
<link rel="stylesheet" href="https://fonts.googleapis.com/css2?family=Rubik:wght@300;400;500;700&display=swap">
<style>
  :root {
    --brand-red: #8e1c16;
    --brand-red-light: #c0625c;
    --text-grey: #444444;
    --dieline: #b5524c;
    --guide-blue: #7cc7e6;
    --paper: #ffffff;
    --photo-dark: #3a3a3a;
    --photo-mid: #8a8a8a;
    --photo-light: #e4e4e4;
  }
  * { margin: 0; padding: 0; box-sizing: border-box; }
  html, body { width: 1200px; height: 900px; overflow: hidden; background: var(--paper); }
  body { font-family: "Rubik", Arial, sans-serif; color: var(--text-grey); }
  .folder { position: relative; width: 1200px; height: 900px; }
  .folder__lines { position: absolute; inset: 0; }

  .cover-photo {
    position: absolute; left: 199px; top: 12px; width: 839px; height: 477px;
    background: linear-gradient(180deg, var(--photo-light) 0%, var(--photo-mid) 45%, var(--photo-dark) 70%, var(--photo-mid) 85%, var(--photo-dark) 100%);
  }
  .cover-frame {
    position: absolute; left: 701px; top: 37px; width: 463px; height: 665px;
    border: 1px solid var(--brand-red);
  }
  .claim {
    position: absolute; top: 204px; writing-mode: vertical-rl; white-space: nowrap; line-height: 1;
  }
  .claim--lead { left: 1106px; font-size: 25px; font-weight: 300; color: var(--text-grey); }
  .claim--key { left: 1066px; top: 248px; font-size: 40px; font-weight: 700; color: var(--brand-red); letter-spacing: 0.5px; }

  .brand { position: absolute; display: flex; flex-direction: column; color: var(--brand-red); font-weight: 500; line-height: 1.1; }
  .brand__square { background: var(--brand-red); margin-bottom: 8px; }
  .brand--flap { right: 1080px; top: 118px; align-items: flex-end; font-size: 13px; text-align: right; }
  .brand--flap .brand__square { width: 26px; height: 26px; }
  .brand--back { left: 199px; top: 566px; font-size: 20px; }
  .brand--back .brand__square { width: 40px; height: 40px; }
  .brand--front { left: 743px; top: 546px; font-size: 20px; }
  .brand--front .brand__square { width: 40px; height: 40px; }

  .flap-contact { position: absolute; right: 1080px; font-size: 8.6px; line-height: 11.2px; text-align: right; }
  .flap-contact--dresden { top: 494px; }
  .flap-contact--south { top: 604px; }
  .flap-contact p + p { margin-top: 11px; }
  .flap-divider { position: absolute; left: 30px; top: 586px; width: 91px; border-top: 1px dotted var(--dieline); }

  .back-contact { position: absolute; right: 587px; top: 576px; text-align: right; font-size: 8.6px; line-height: 11px; }
  .back-contact__address { margin-bottom: 10px; }
  .back-contact__web { margin-top: 17px; font-size: 20px; font-weight: 300; line-height: 24px; color: var(--brand-red-light); }

  .front-web { position: absolute; right: 72px; top: 648px; font-size: 13px; color: var(--text-grey); }
</style>
</head>
<body>
<main class="folder">
  <svg class="folder__lines" width="1200" height="900" viewBox="0 0 1200 900" aria-hidden="true">
    <g fill="none" stroke="var(--dieline)" stroke-width="0.8" stroke-dasharray="2 2">
      <path d="M140 12 H1188 V730 H660"/>
      <path d="M140 12 L35 36 Q12 44 12 66 V690 Q12 706 34 710 L140 730"/>
      <path d="M149 742 L184 777 V790 L176 784 Q164 800 168 820 Q180 855 222 860 Q240 858 248 850 L242 846 L250 846 L280 872 H612 Q634 872 640 850 L660 730"/>
    </g>
    <g stroke="var(--guide-blue)" stroke-width="0.7">
      <line x1="140" y1="12" x2="140" y2="730"/>
      <line x1="149" y1="12" x2="149" y2="730"/>
      <line x1="660" y1="12" x2="660" y2="730"/>
      <line x1="676" y1="12" x2="676" y2="730"/>
      <line x1="149" y1="730" x2="660" y2="730"/>
      <line x1="149" y1="742" x2="660" y2="742"/>
    </g>
  </svg>

  <div class="cover-photo" role="img" aria-label="Schwarz-Weiß-Panorama einer Altstadt am Fluss bei Abenddämmerung mit Kirchtürmen, Brücke und Raddampfern"></div>
  <div class="cover-frame"></div>
  <p class="claim claim--lead">Ihre Zufriedenheit ist unsere</p>
  <p class="claim claim--key">MOTIVATION</p>

  <div class="brand brand--flap"><span class="brand__square"></span><span>Wertbau Elbland AG</span></div>
  <div class="flap-contact flap-contact--dresden">
    <p>Lindenhofweg 12,<br>01468 Moritzburg</p>
    <p>Telefon:<br>03 51 – 48 26 10-20<br>Telefax:<br>03 51 – 48 26 10-21</p>
  </div>
  <div class="flap-divider"></div>
  <div class="flap-contact flap-contact--south">
    <p>Kastanienallee 7<br>89518 Heidenheim</p>
    <p>Telefon:<br>+49 7321 550812<br>Telefax:<br>+49 7321 55081</p>
  </div>

  <div class="brand brand--back"><span class="brand__square"></span><span>Wertbau Elbland AG</span></div>
  <div class="back-contact">
    <p class="back-contact__address">Lindenhofweg 12, 01468 Moritzburg</p>
    <p>Telefon: 03 51 – 48 26 10-20<br>Telefax: 03 51 – 48 26 10-21</p>
    <p class="back-contact__web">info@wbe-ag.de<br>www.wbe-ag.de</p>
  </div>

  <div class="brand brand--front"><span class="brand__square"></span><span>Wertbau Elbland AG</span></div>
  <p class="front-web">www.wbe-ag.de</p>
</main>
</body>
</html>
```